The Brindle Tap Pub Needs A Bottle Label Design

Our gin supplier has created a fantastic bespoke Gin for our micro pub.
The new gin has serval blended ingredients and will be on sale from the 1st July 2017.
The bottle will be a clear 700ml glass style, similar to the attached picture. We would like the design to look as though it has been hand drawn on to the bottle, (line art style) and the background should be transparent.
Once we have confirmed the alcohol volume, this will be need to be included. We believe it to be aprox 40% abv.
Our pub is situated in the Old Swan area of Liverpool, UK and we would be happy for a Swan silhouette and line drawn ingredients to be part of the design.

The label design should have the following text:
The Brindle Tap Gin #1

```html
<!DOCTYPE html>
<html lang="en">
<head>
<meta charset="utf-8">
<title>The Brindle Tap Gin #1 – Bottle Label</title>
<link rel="stylesheet" href="https://fonts.googleapis.com/css2?family=Anton&family=Griffy&display=swap">
<style>
  :root {
    --paper: #ffffff;
    --ink: #000000;
    --gin-blue: #1b74bf;
    --frame: #222222;
  }
  * { box-sizing: border-box; margin: 0; padding: 0; }
  html, body {
    width: 1200px;
    height: 850px;
    overflow: hidden;
    background: var(--paper);
  }
  .canvas {
    position: relative;
    width: 1200px;
    height: 850px;
  }
  .label {
    position: absolute;
    left: 290px;
    top: 15px;
    width: 620px;
    height: 820px;
    border: 1px solid var(--frame);
    background: var(--paper);
    font-family: "Anton", "Arial Narrow", sans-serif;
    color: var(--ink);
  }
  .label__pub {
    position: absolute;
    left: 41px;
    top: 46px;
    height: 61px;
    padding: 0 12px;
    background: var(--ink);
    color: var(--paper);
    font-size: 33px;
    line-height: 61px;
    white-space: nowrap;
  }
  .label__title {
    position: absolute;
    right: 47px;
    top: 78px;
    font-family: "Griffy", cursive;
    font-weight: 400;
    font-size: 104px;
    line-height: 1;
    color: var(--gin-blue);
    white-space: nowrap;
  }
  .label__with {
    position: absolute;
    right: 50px;
    top: 240px;
    font-size: 40px;
    line-height: 1;
  }
  .botanicals {
    position: absolute;
    right: 45px;
    top: 293px;
    list-style: none;
    display: flex;
    flex-direction: column;
    align-items: flex-end;
    gap: 12px;
  }
  .botanicals__item {
    height: 38px;
    padding: 0 8px;
    background: var(--ink);
    color: var(--paper);
    font-size: 26px;
    line-height: 38px;
    white-space: nowrap;
  }
  .swan {
    position: absolute;
    left: 48px;
    top: 285px;
    width: 318px;
    height: 390px;
  }
  .label__abv {
    position: absolute;
    left: 500px;
    top: 646px;
    width: 60px;
    text-align: center;
    font-size: 27px;
    line-height: 32px;
  }
  .label__volume {
    position: absolute;
    left: 220px;
    top: 708px;
    width: 166px;
    text-align: center;
    font-size: 44px;
    line-height: 1.1;
  }
</style>
</head>
<body>
<main class="canvas">
  <section class="label">
    <div class="label__pub">The Brindle Tap</div>
    <h1 class="label__title">Gin #1</h1>
    <p class="label__with">with:</p>
    <ul class="botanicals">
      <li class="botanicals__item">Juniper berries</li>
      <li class="botanicals__item">Cardamon</li>
      <li class="botanicals__item">Cubebs</li>
      <li class="botanicals__item">Grapefruit</li>
      <li class="botanicals__item">Ginger</li>
      <li class="botanicals__item">Otis root</li>
    </ul>
    <svg class="swan" viewBox="0 0 318 390" role="img" aria-label="Black line-art swan silhouette with sweeping wing and curled neck">
      <defs>
        <radialGradient id="swanFill" cx="50%" cy="55%" r="60%">
          <stop offset="0%" stop-color="#3a3a3a"/>
          <stop offset="100%" stop-color="#111111"/>
        </radialGradient>
      </defs>
      <rect width="318" height="390" fill="url(#swanFill)"/>
    </svg>
    <p class="label__abv">42%<br>ABV</p>
    <p class="label__volume">700ml</p>
  </section>
</main>
</body>
</html>
```